Professional Lawn Treatment flyer (double sided) needed for established gardening company

We are an established and trusted gardening company in Swindon, UK, and are about to launch a new Lawn Treatment Service. This will be marketed to both existing and new customers and needs to reflect our current professional image. The flyer will need to be double-sided, portrait orientation and correctly sized so to be printed on A5.

If you look on our website www.tavistrowgardening.co.uk, you will see our colours are purple and green. We would like you to use these exact shades of purple and green in your design.

As part of the design, we will need you to put together an infographic table to show our packages. I have attached a spreadsheet which explains these packages but I will need you to create a visually appealing table that fits in with the overall design of the flyer. I don't want you to simply cut and paste my basic table into the design.

In terms of what needs to be included, I have tried to be as specific as possible here but please feel free to message me if you need any further information or clarification.

FRONT SIDE:
The title of our service is:
Expert Lawn Treatment Service

Our strapline will need to be included somewhere:
"Lawn care by your local gardening expert"

The front side of the flyer will need to contain our logo - different versions of which can be found within my dropbox folder here...

https://www.sharebinnu.co.uk/sh/k7qd21mzplax/QRT8xWbnNeLu4Pa-ZxYyhKcLo?dl=0

The front side will need to contain a main image (although feel free to add more if you have anything suitable). I have included a picture in the dropbox folder titled "Front side image" which we would like used. I've also included in the folder an adobe image of grass which you may or may not like to use on either front or back.

Somewhere on both the front and back sides, you will need to include our contact details:
01632 960417
www.tavistrowgardening.co.uk/lawncare

The front side should show what treatments we currently have available. These are:

- Lawn Fertilising
- Scarification
- Aeration
- Weed Control
- Moss Control
- Hydration Booster
- PlumeRest
- Turfing & Renovation

"Select a one-off treatment or choose from one of our specially created lawn care packages."

BACK SIDE:
On the back, we will still need our logo and contact details but the image we'd like used should be the one in the dropbox folder titled "Back side image". Again, if you have any other images you feel would also work, then please feel free to add them.

The back side is to contain a bit more information and be a bit 'wordier' and so can you please include the following 2 paragraphs:

"As expert gardeners, we are passionate about horticulture and working to bring out the very best in your garden. When we work in your garden, we look at it and treat it with the same care and attention as if it were our own, before handing it back for you to enjoy. Our passion doesn't end at just trees and shrubs though. Your grass is as much of a living, breathing plant as your shrubs and we therefore utilise our expert horticultural knowledge to ensure your lawn thrives and reaches its fullest potential.

Lawn care isn't just about applying a fertiliser. It's about really understanding your lawn and being able to use extensive knowledge and experience to diagnose and treat issues. It therefore stands to reason that you should employ an expert to bring out the best in your lawn which is why we at Tavistrow Gardening Services have created a superior lawn care service that will keep your lawn looking lush, green and healthy all year round."

I referred at the very top of this brief to the fact we will need an infographic table created to show the different lawn care packages available. You see from the PDF table I created that we have 3 packages; Standard, Enhanced and Premium. Please create a visually appealing table which sets out the differences between our packages and include it on the back page.

Finally, somewhere we would like reference to the other gardening services we do. It's only to be something small as it isn't the main focus of the flyer but we think it would be good to mention what else we do. To re-iterate, it isnt to be big. I still want the main focus to be lawn care but if you could somehow reference that we also do the following services, that would be good. I will leave it to you to decide where on the flyer it fits in best, be it the front or back:

- Lawn mowing
- Shrub pruning
- Hedge trimming
- Weed killing
- Garden clearance & tidy-up
- Planting & design
- Regular Garden Maintenance
- Turfing
- Fencing
- Gutter clearance

I think thats it. I look forward to your designs!
Ps. Don't forget the dropbox folder:

Target Market(s)

Professional men/women aged 25+
Retired aged 65+

Industry/Entity Type

Home And Garden

Font styles to use
Sans Serif

Colors
6b449b
9bcb3c

Requirements
Must have
• Our company colours; purple and green; as per our website www.tavistrowgardening.co.uk. I've selected purple and green on this brief just to highlight the colours needed but please be sure to use the exact shades from our website and NOT the shade of purple and green that were selected on this brief.
• All the wording as explained in the main project brief.
Nice to have
• I want the flyer to be bold, eye-catching and modern.
• We particularly like the font Trebuchet MS for general copy but please feel free to use any other font for bolder, main titles.
Should not have
• We don't want anything gimmicky. No cheesy marketing.
• We only want professional looking designs. With the greatest of respect, if you're just starting out or don't really do design but think you'll use this as practise, please don't waste your or our time. We've previously run contests for other projects where we've had designs submitted that have clearly been done on MS Word and used Clipart and Wordart. That's really not what we are looking for.

```html
<!DOCTYPE html>
<html lang="en">
<head>
<meta charset="utf-8">
<title>Tavistrow Gardening Services – Lawn Treatment Flyer</title>
<link href="https://fonts.googleapis.com/css2?family=Ubuntu:wght@400;500;700&display=swap" rel="stylesheet">
<style>
  :root{
    --purple:#77297f;
    --green:#3fb54a;
    --green-light:#8fd07a;
    --green-dark:#14572c;
    --white:#ffffff;
    --grass-1:#5d9a2c;
    --grass-2:#9ccd4a;
  }
  *{margin:0;padding:0;box-sizing:border-box}
  html,body{width:1200px;height:1200px;overflow:hidden;background:#fff}
  body{font-family:'Ubuntu',sans-serif;color:var(--white)}
  .stage{position:relative;width:1200px;height:1200px;background:#fff}
  .flyer{position:absolute;transform-origin:0 0;transform:scale(.8);overflow:hidden;
    box-shadow:0 3px 10px rgba(0,0,0,.28)}
  .flyer--front{left:70px;top:166px;width:640px;height:908px;background:var(--purple)}
  .flyer--back{left:631px;top:285px;width:641px;height:908px;background:var(--green)}
  .abs{position:absolute}

  /* FRONT */
  .band-green{left:0;top:50px;width:100%;height:20px;background:var(--green)}
  .hero-photo{left:0;top:104px;width:100%;height:300px;
    background:linear-gradient(180deg,#6e8f52 0%,#4f9a2a 30%,#63b135 60%,#c7c4b8 85%,#8fc24a 100%)}
  .logo-oval{left:172px;top:27px;width:296px;height:150px;border-radius:50%;background:var(--white);
    border:5px solid var(--green);display:flex;align-items:center;justify-content:center;text-align:center;gap:8px}
  .logo-dot{width:16px;height:16px;border-radius:50%;background:var(--green)}
  .logo-name{font-weight:500;color:var(--green-dark);font-size:22px;line-height:1.15}
  .title-band{left:0;top:399px;width:100%;height:160px;background:var(--green)}
  .title{left:24px;top:414px;font-family:'Ubuntu',sans-serif;font-weight:500;font-size:62px;line-height:58px;
    white-space:nowrap;transform:scaleX(.76);transform-origin:0 0}
  .circle{border-radius:50%;border:4px solid var(--white)}
  .circle--mower{left:414px;top:305px;width:150px;height:150px;background:radial-gradient(circle at 50% 70%,#4fae2d,#3a6b2a 70%,#6d6253)}
  .circle--turf{left:519px;top:399px;width:132px;height:132px;background:radial-gradient(circle at 40% 40%,#6bb33d,#5a4a38 80%)}
  .strapline{left:0;top:537px;width:532px;height:33px;background:var(--white);white-space:nowrap;
    clip-path:polygon(0 0,96% 0,100% 100%,0 100%);color:var(--green);font-weight:700;font-size:20px;
    padding:5px 0 0 13px}
  .intro{left:24px;top:600px;width:360px;font-size:15.5px;line-height:25px}
  .enquiry{left:0;top:679px;width:391px;height:160px;background:var(--green);text-align:center}
  .enquiry-label{font-size:19px;margin-top:22px}
  .enquiry-phone{font-weight:500;font-size:46px;line-height:50px;margin-top:4px;white-space:nowrap;
    transform:scaleX(.8);transform-origin:50% 0}
  .enquiry-url{font-size:18px;margin-top:0;white-space:nowrap}
  .treatments{left:415px;top:597px;list-style:none;font-size:18px;font-weight:500;line-height:27.4px}
  .bullet-list li{white-space:nowrap}
  .bullet-list li::before{content:"";display:inline-block;width:8px;height:8px;border-radius:50%;background:var(--white);margin-right:8px;vertical-align:2px}
  .grass-strip{left:0;top:822px;width:100%;height:86px;background:linear-gradient(180deg,rgba(120,190,60,.0) 0%,var(--grass-2) 35%,var(--grass-1) 100%)}

  /* BACK */
  .back-top{left:0;top:0;width:100%;height:30px;background:var(--purple)}
  .back-photo{left:0;top:40px;width:100%;height:352px;
    background:linear-gradient(180deg,#6f6a55 0%,#5f7d3a 30%,#5ea23a 55%,#8fa06f 80%,#64913a 100%)}
  .table-tab{left:71px;top:121px;width:275px;height:32px;background:var(--white);border-radius:10px 10px 0 0;
    color:var(--green);font-weight:700;font-size:18px;text-align:center;padding-top:5px;white-space:nowrap}
  .packages{left:22px;top:152px;width:356px;border-collapse:collapse;font-size:11.5px;font-weight:500}
  .packages th{font-weight:500;font-size:11px;line-height:13px;height:40px;vertical-align:middle;text-align:center}
  .packages td{height:23px;border-bottom:1px solid rgba(255,255,255,.55);white-space:nowrap}
  .packages td.label{padding-left:12px;background:rgba(63,181,74,.88);width:186px}
  .packages .col-standard{background:rgba(143,208,122,.9);width:56px;text-align:center}
  .packages .col-enhanced{background:rgba(63,181,74,.92);width:57px;text-align:center}
  .packages .col-premium{background:var(--purple);width:57px;text-align:center}
  .packages thead .label-head{background:rgba(63,181,74,.88)}
  .about{left:18px;top:405px;width:350px;font-size:16px;line-height:20.3px;text-align:justify;hyphens:none}
  .about p+p{margin-top:20px}
  .services-head{left:391px;top:337px;width:240px;height:104px;background:var(--white);border-radius:14px 14px 0 0;
    color:var(--green-dark);font-weight:700;font-size:44px;line-height:42px;padding:16px 0 0 16px}
  .services{left:391px;top:439px;width:240px;height:300px;background:var(--purple);list-style:none;
    font-size:16px;font-weight:500;line-height:27.4px;padding:17px 0 0 6px}
  .services li::before{margin-right:4px}
  .thumb{top:741px;height:116px;border:3px solid var(--white)}
  .thumb--grass{left:391px;width:122px;background:linear-gradient(180deg,#a7d66a,#4f9a24)}
  .thumb--spreader{left:515px;width:126px;background:linear-gradient(180deg,#4e5e3a,#8ea35e 60%,#6e9a44)}
  .back-footer{left:0;top:859px;width:100%;height:49px;background:var(--purple);text-align:center;
    font-weight:700;font-size:26px;padding-top:7px;white-space:nowrap}
</style>
</head>
<body>
<div class="stage">

  <section class="flyer flyer--front">
    <div class="abs band-green"></div>
    <div class="abs hero-photo" role="img" aria-label="Garden lawn with curving stone path"></div>
    <div class="abs logo-oval">
      <span class="logo-dot"></span>
      <span class="logo-name">Tavistrow<br>Gardening Services</span>
    </div>
    <div class="abs title-band"></div>
    <h1 class="abs title">EXPERT LAWN<br>TREATMENT SERVICE</h1>
    <div class="abs circle circle--mower" role="img" aria-label="Lawn mower on grass"></div>
    <div class="abs circle circle--turf" role="img" aria-label="Gloved hand laying turf roll"></div>
    <div class="abs strapline">LAWN CARE by YOUR LOCAL GARDENING EXPERT</div>
    <p class="abs intro">Select a one-off treatment or choose from one of our specially created lawn care packages.</p>
    <div class="abs grass-strip" role="img" aria-label="Close-up of green grass blades"></div>
    <div class="abs enquiry">
      <p class="enquiry-label">For Enquiry:</p>
      <p class="enquiry-phone">CALL 01632 960417</p>
      <p class="enquiry-url">www.tavistrowgardening.co.uk/lawncare</p>
    </div>
    <ul class="abs treatments bullet-list">
      <li>Lawn Fertilising</li>
      <li>Scarification</li>
      <li>Aeration</li>
      <li>Weed Control</li>
      <li>Moss Control</li>
      <li>Hydration Booster</li>
      <li>PlumeRest</li>
      <li>Turfing &amp; Renovation</li>
    </ul>
  </section>

  <section class="flyer flyer--back">
    <div class="abs back-top"></div>
    <div class="abs back-photo" role="img" aria-label="Striped lawn with paved path and planted borders"></div>
    <div class="abs table-tab">LAWN TREATMENT PACKAGES</div>
    <table class="abs packages">
      <thead>
        <tr><th class="label-head"></th><th class="col-standard">Standard<br>Package</th><th class="col-enhanced">Enhanced<br>Package</th><th class="col-premium">Premium<br>Package</th></tr>
      </thead>
      <tbody>
        <tr><td class="label">Spring Treatment</td><td class="col-standard">✔</td><td class="col-enhanced">✔</td><td class="col-premium">✔</td></tr>
        <tr><td class="label">Early Summer Treatment</td><td class="col-standard">✔</td><td class="col-enhanced">✔</td><td class="col-premium">✔</td></tr>
        <tr><td class="label">Late Summer Treatment</td><td class="col-standard">✔</td><td class="col-enhanced">✔</td><td class="col-premium">✔</td></tr>
        <tr><td class="label">Autumn/Winter Treatment</td><td class="col-standard">✔</td><td class="col-enhanced">✔</td><td class="col-premium">✔</td></tr>
        <tr><td class="label">Scarification</td><td class="col-standard"></td><td class="col-enhanced">✔</td><td class="col-premium">✔</td></tr>
        <tr><td class="label">Aeration</td><td class="col-standard"></td><td class="col-enhanced">✔</td><td class="col-premium">✔</td></tr>
        <tr><td class="label">PlumeRest Treatment</td><td class="col-standard"></td><td class="col-enhanced"></td><td class="col-premium">✔</td></tr>
        <tr><td class="label">Hydration Boost Treatment</td><td class="col-standard"></td><td class="col-enhanced"></td><td class="col-premium">✔</td></tr>
      </tbody>
    </table>
    <div class="abs about">
      <p>As expert gardeners, we are passionate about horticulture and working to bring out the very best in your garden. When we work in your garden, we look at it and treat it with the same care and attention as if it were our own, before handing it back for you to enjoy. Our passion doesn't end at just trees and shrubs though. Your grass is as much of a living, breathing plant as your shrubs and we therefore utilise our expert horticultural knowledge to ensure your lawn thrives and reaches its fullest potential.</p>
      <p>Lawn care isn't just about applying a fertiliser. It's about really understanding your lawn and being able to use extensive knowledge and experience to diagnose and treat issues. It therefore stands to reason that you should employ an expert to bring out the best in your lawn which is why we at Tavistrow Gardening Services have created a superior lawn care service that will keep your lawn looking lush, green and healthy all year round."</p>
    </div>
    <h2 class="abs services-head">GARDEN<br>SERVICE</h2>
    <ul class="abs services bullet-list">
      <li>Lawn mowing</li>
      <li>Shrub pruning</li>
      <li>Hedge trimming</li>
      <li>Weed killing</li>
      <li>Garden clearance &amp; tidy-up</li>
      <li>Planting &amp; design</li>
      <li>Regular Garden Maintenance</li>
      <li>Turfing</li>
      <li>Fencing</li>
      <li>Gutter clearance</li>
    </ul>
    <div class="abs thumb thumb--grass" role="img" aria-label="Close-up of lush lawn"></div>
    <div class="abs thumb thumb--spreader" role="img" aria-label="Fertiliser spreader on lawn"></div>
    <div class="abs back-footer">www.tavistrowgardening.co.uk</div>
  </section>

</div>
</body>
</html>
```